Business Card Colourful and fun Design Project

I need a business card design for my Ecommerce website which am launching soon. we are based in the United Arab Emirates and our customers are based in Dubai and other cities in UAE, In addition to our neighbour countries in the GCC. We sell Gadgets, fashion and other trendy stuff that are hard to find in our market. The company name is "ZIMTOWALRUS" logo consists of a panda wearing traditional local Arab thobe. would like to see a clean, colourful fun design to represent us.
Updates
please read the discussion board. thanks
Industry/Entity Type
Fashion
Look and feel
Each slider illustrates characteristics of the customer's brand and the style your logo design should communicate.

```html
<!DOCTYPE html>
<html lang="en">
<head>
<meta charset="utf-8">
<title>ZIMTOWALRUS business card</title>
<link rel="stylesheet" href="https://fonts.googleapis.com/css2?family=Source+Sans+3:wght@400;600&display=swap">
<style>
  :root {
    --brand-red: #be1e2d;
    --ink: #111111;
    --paper: #ffffff;
    --mark-grey: #dcdcdc;
  }
  html, body {
    margin: 0;
    padding: 0;
    overflow: hidden;
    background: var(--paper);
  }
  .canvas {
    position: relative;
    width: 1200px;
    height: 978px;
    overflow: hidden;
    background: var(--paper);
    font-family: "Source Sans 3", "Myriad Pro", Arial, sans-serif;
  }
  .artwork {
    position: absolute;
    inset: 0;
  }
  .brand-square {
    position: absolute;
    background: var(--mark-grey);
  }
  .brand-square--front { left: 140px; top: 150px; width: 80px; height: 80px; }
  .brand-square--back  { left: 902px; top: 410px; width: 56px; height: 56px; }
  .brand-name {
    position: absolute;
    margin: 0;
    color: var(--brand-red);
    font-weight: 600;
    letter-spacing: 1.5px;
    line-height: 1;
    white-space: nowrap;
  }
  .brand-name--front { left: 244px; top: 182px; font-size: 37px; }
  .brand-name--back  { left: 816px; top: 508px; font-size: 37px; }
  .holder-name {
    position: absolute;
    left: 196px;
    top: 510px;
    margin: 0;
    color: var(--brand-red);
    font-size: 42px;
    font-weight: 400;
    line-height: 1;
    white-space: nowrap;
  }
  .holder-role {
    position: absolute;
    left: 350px;
    top: 548px;
    margin: 0;
    color: var(--ink);
    font-size: 21px;
    line-height: 1;
    white-space: nowrap;
  }
  .contact-list {
    position: absolute;
    left: 114px;
    top: 707px;
    margin: 0;
    padding: 0;
    list-style: none;
    color: var(--ink);
    font-size: 22.5px;
    line-height: 27.4px;
    white-space: nowrap;
  }
</style>
</head>
<body>
<main class="canvas">
  <svg class="artwork" width="1200" height="978" viewBox="0 0 1200 978" aria-hidden="true">
    <g class="card-front">
      <path d="M2,2 H400 Q551,2 551,155 V950 H2 Z" fill="var(--paper)" stroke="var(--brand-red)" stroke-width="3"/>
      <path fill="var(--brand-red)" d="M8,0 H135 L98,38 L86,385 C120,410 170,395 235,330 C300,300 400,290 460,272 C510,262 540,300 553,335 V388 C520,370 490,345 460,360 C420,380 360,372 318,348 C300,380 270,400 230,415 C190,430 175,470 165,540 C150,580 140,600 125,640 C110,680 85,700 70,705 L66,945 L8,945 Z"/>
      <g fill="var(--paper)">
        <rect x="0" y="0" width="30" height="104"/>
        <rect x="0" y="218" width="26" height="112"/>
        <rect x="0" y="330" width="65" height="110"/>
        <rect x="0" y="555" width="64" height="115"/>
        <rect x="0" y="780" width="62" height="110"/>
      </g>
      <path fill="var(--brand-red)" d="M80,945 L490,893 L553,848 V952 H80 Z"/>
    </g>
    <g class="card-back">
      <path d="M651,24 H1045 Q1196,24 1196,175 V975 H651 Z" fill="var(--paper)" stroke="var(--brand-red)" stroke-width="3"/>
      <path fill="var(--brand-red)" d="M652,365 C690,395 705,455 682,545 C668,525 660,512 652,500 Z"/>
    </g>
  </svg>

  <div class="brand-square brand-square--front" aria-hidden="true"></div>
  <p class="brand-name brand-name--front">ZIMTOWALRUS</p>

  <h1 class="holder-name">Simple Text</h1>
  <p class="holder-role">Designation</p>

  <ul class="contact-list">
    <li>TEL&nbsp; 3546-10293847</li>
    <li>Fax-0218 -730 -2861</li>
    <li>Adress :&nbsp; 12 Palm Crescent Street</li>
    <li>DUBAI UAE</li>
    <li>www-zimtowalrus.com</li>
    <li>info@zimtowalrus.com</li>
  </ul>

  <div class="brand-square brand-square--back" aria-hidden="true"></div>
  <p class="brand-name brand-name--back">ZIMTOWALRUS</p>
</main>
</body>
</html>
```